label update for bottle change

The goal is to adapt the label's design and shape to the new bottle, maintaining its defining elements such as the font, vertical name, company logo, background pattern, and color. The new design should not be identical to the old one, but rather an evolution of it. The gold stripe on the bottom is not mandatory, but the writing "BORGO DEL VALLONE / EST. 1886" must be retained, slightly enlarged.

The font name is: Brandon Text

```html
<!DOCTYPE html>
<html lang="it">
<head>
<meta charset="utf-8">
<title>Amaro di Carattere Carciofo – Etichetta</title>
<link rel="stylesheet" href="https://fonts.googleapis.com/css2?family=Josefin+Sans:wght@300;400;700&display=swap">
<style>
  :root {
    --stage: #d9d9d9;
    --purple: #44095c;
    --gold: #d9b25a;
    --gold-light: #f1d98e;
    --white: #ffffff;
  }
  html, body {
    margin: 0;
    width: 1200px;
    height: 1200px;
    overflow: hidden;
    background: var(--stage);
  }
  .label {
    position: absolute;
    left: 215px;
    top: 72px;
    width: 768px;
    height: 1055px;
    background: var(--purple);
    overflow: hidden;
    font-family: "Josefin Sans", sans-serif;
    color: var(--white);
  }
  .maker {
    position: absolute;
    right: 70px;
    top: 106px;
    text-align: right;
    line-height: 1;
  }
  .maker-line {
    display: block;
    font-size: 13px;
    font-weight: 700;
    letter-spacing: 0.32em;
    margin-right: -0.32em;
  }
  .maker-name {
    display: block;
    margin-top: 8px;
    font-size: 30px;
    font-weight: 700;
    letter-spacing: 0.01em;
  }
  .vertical {
    position: absolute;
    writing-mode: vertical-rl;
    transform: rotate(180deg);
    white-space: nowrap;
    line-height: 1;
  }
  .product-name {
    left: 142px;
    bottom: 158px;
    font-size: 106px;
    font-weight: 700;
    letter-spacing: 0.05em;
  }
  .product-type {
    left: 88px;
    bottom: 152px;
    font-size: 33px;
    font-weight: 300;
    letter-spacing: 0;
  }
  .origin {
    position: absolute;
    left: 89px;
    top: 960px;
    font-size: 25px;
    font-weight: 300;
    letter-spacing: 0.02em;
    white-space: nowrap;
  }
  .flower {
    position: absolute;
    left: 291px;
    top: 340px;
    width: 438px;
    height: 715px;
  }
</style>
</head>
<body>
  <main class="label">
    <div class="maker">
      <span class="maker-line">FABBRICA LIQUORI</span>
      <span class="maker-name">F.LLI MARCHETTI</span>
    </div>

    <div class="vertical product-type">AMARO DI CARATTERE</div>
    <div class="vertical product-name">CARCIOFO</div>

    <svg class="flower" role="img" aria-label="Gold line illustration of a lotus-like flower in bloom on a long stem" viewBox="0 0 438 715">
      <defs>
        <radialGradient id="flowerGlow" cx="50%" cy="45%" r="50%">
          <stop offset="0%" stop-color="#f1d98e" stop-opacity="0.32"/>
          <stop offset="55%" stop-color="#d9b25a" stop-opacity="0.14"/>
          <stop offset="100%" stop-color="#d9b25a" stop-opacity="0"/>
        </radialGradient>
      </defs>
      <rect width="438" height="715" fill="url(#flowerGlow)"/>
    </svg>

    <div class="origin">BORGO DEL VALLONE / EST. 1886</div>
  </main>
</body>
</html>
```